Lakemont Hydro Partners, Inc. Company Brochure

I would like someone to design a brochure that can be handed out to prospective clients. We are a full service water and wastewater operations company that provides services to Municipal Utility Districts and citys. I would like something that is catchy to the eye and reflects a company that prides itself on providing personal service to its clients. We need to revamp our website, that's next, but the website does have a description of our company and services offered. You can find that information at www.lakemonthydropartners.example

```html
<!DOCTYPE html>
<html lang="en">
<head>
<meta charset="utf-8">
<title>Lakemont Hydro Partners, Inc. – Brochure Inside Pages</title>
<link rel="stylesheet" href="https://fonts.googleapis.com/css2?family=Montserrat:wght@700;800&family=Hind:wght@400&family=Arimo:wght@400&display=swap">
<style>
  :root {
    --page-bg: #ffffff;
    --aqua-deep: #a9f1f6;
    --aqua-soft: #e6fbfc;
    --aqua-line: #1de4ef;
    --brand-blue: #1459c8;
    --body-ink: #2b2b2b;
    --label-ink: #3a3a3a;
    --page-edge: #8a8a8a;
  }
  html, body {
    margin: 0;
    padding: 0;
    overflow: hidden;
    background: var(--page-bg);
  }
  .canvas {
    position: relative;
    width: 1200px;
    height: 1000px;
    overflow: hidden;
    background: var(--page-bg);
  }
  .spread-art {
    position: absolute;
    inset: 0;
  }
  .panel-copy {
    position: absolute;
    text-align: center;
  }
  .panel-copy--about { left: 236px; top: 306px; width: 270px; }
  .panel-copy--mission { left: 722px; top: 306px; width: 270px; }
  .panel-title {
    margin: 0;
    font-family: "Montserrat", sans-serif;
    font-weight: 800;
    color: var(--brand-blue);
    line-height: 1;
  }
  .panel-title__main {
    display: block;
    font-size: 23px;
    letter-spacing: 0.5px;
  }
  .panel-title__sub {
    display: block;
    font-size: 13.5px;
    margin-top: 3px;
    letter-spacing: 0.6px;
  }
  .panel-body {
    margin: 12px 0 0;
    font-family: "Hind", sans-serif;
    font-weight: 400;
    color: var(--body-ink);
    font-size: 7.6px;
    line-height: 10.6px;
  }
  .panel-copy--mission .panel-body {
    font-size: 8.4px;
    line-height: 11.6px;
    margin: 0 -14px;
    margin-top: 12px;
  }
  .page-label {
    position: absolute;
    top: 728px;
    width: 200px;
    text-align: center;
    font-family: "Arimo", sans-serif;
    font-size: 18px;
    color: var(--label-ink);
  }
  .page-label--left { left: 293px; }
  .page-label--right { left: 662px; }
</style>
</head>
<body>
<div class="canvas">
  <svg class="spread-art" width="1200" height="1000" viewBox="0 0 1200 1000" xmlns="http://www.w3.org/2000/svg">
    <defs>
      <linearGradient id="aquaLeft" x1="0" y1="0" x2="1" y2="1">
        <stop offset="0" stop-color="var(--aqua-deep)"/>
        <stop offset="0.55" stop-color="#c8f6f9"/>
        <stop offset="1" stop-color="var(--aqua-soft)"/>
      </linearGradient>
      <linearGradient id="aquaRight" x1="1" y1="0" x2="0" y2="1">
        <stop offset="0" stop-color="var(--aqua-deep)"/>
        <stop offset="0.55" stop-color="#c8f6f9"/>
        <stop offset="1" stop-color="var(--aqua-soft)"/>
      </linearGradient>
      <linearGradient id="photoPlant" x1="0" y1="0" x2="1" y2="1">
        <stop offset="0" stop-color="#6f7c86"/>
        <stop offset="1" stop-color="#2f3a40"/>
      </linearGradient>
      <linearGradient id="photoAerator" x1="0" y1="0" x2="0" y2="1">
        <stop offset="0" stop-color="#6f8a78"/>
        <stop offset="0.5" stop-color="#c9dcd6"/>
        <stop offset="1" stop-color="#5d7c74"/>
      </linearGradient>
      <linearGradient id="photoDrinking" x1="0" y1="0" x2="0" y2="1">
        <stop offset="0" stop-color="#7fbf3a"/>
        <stop offset="0.6" stop-color="#cfe7d9"/>
        <stop offset="1" stop-color="#4aa9de"/>
      </linearGradient>
      <linearGradient id="photoOperator" x1="0" y1="0" x2="1" y2="1">
        <stop offset="0" stop-color="#5f9fe0"/>
        <stop offset="0.6" stop-color="#8a8f7a"/>
        <stop offset="1" stop-color="#d9733a"/>
      </linearGradient>
    </defs>

    <!-- left inside page -->
    <g class="page page--about">
      <path class="page-shape" fill="url(#aquaLeft)"
            d="M365,720 A235,235 0 1 1 531,319 C580,368 600,500 600,720 Z"/>
      <path class="copy-arch" fill="#ffffff" stroke="var(--aqua-line)" stroke-width="3"
            d="M222,565 V421 A149,149 0 0 1 520,421 V565"/>
      <line class="photo-link" x1="330" y1="570" x2="420" y2="570" stroke="var(--aqua-line)" stroke-width="3"/>
      <circle class="photo-spot" cx="310" cy="570" r="65" fill="url(#photoPlant)"
              role="img" aria-label="Aerial view of a circular wastewater clarifier at a treatment plant"/>
      <circle class="photo-spot" cx="472" cy="595" r="90" fill="url(#photoAerator)"
              role="img" aria-label="Paddle-wheel aerator splashing water in a treatment pond"/>
    </g>

    <!-- right inside page -->
    <g class="page page--mission">
      <path class="page-shape" fill="url(#aquaRight)" stroke="var(--page-edge)" stroke-width="0.8"
            d="M835,720 A235,235 0 1 0 669,319 C620,368 600,500 600,720 Z"/>
      <path class="copy-arch" fill="#ffffff" stroke="var(--aqua-line)" stroke-width="3"
            d="M710,565 V428 A147,147 0 0 1 1004,428 V565"/>
      <line class="photo-link" x1="840" y1="575" x2="890" y2="575" stroke="var(--aqua-line)" stroke-width="3"/>
      <circle class="photo-spot" cx="755" cy="582" r="103" fill="url(#photoDrinking)"
              role="img" aria-label="Child drinking clean water from a bottle outdoors"/>
      <circle class="photo-spot" cx="942" cy="550" r="72" fill="url(#photoOperator)"
              role="img" aria-label="Plant operator in hard hat and safety vest checking a clipboard"/>
    </g>
  </svg>

  <section class="panel-copy panel-copy--about">
    <h2 class="panel-title">
      <span class="panel-title__main">ABOUT</span>
      <span class="panel-title__sub">OUR COMPANY</span>
    </h2>
    <p class="panel-body">Lakemont Hydro Partners, Inc. was incorporated in the state of Texas in 1989 and is a leading competitor in the water and waste water operations industry. We are a "full service" operations company that handles all aspects of operations in the water/ wastewater industry. All personnel employed by Lakemont Hydro Partners, Inc. are licensed by the TCEQ in water and waste water operations and obtain the proper training needed to successfully operate treatment plants to their maximum capability. We are certified to operate surface water, ground water and wastewater treatment facilities. Here at Lakemont Hydro Partners, Inc. we feel that it is important to provide the highest caliber of services available to the Districts in which we operate. We offer the ability to tailor our services based on the current needs of the District.</p>
  </section>

  <section class="panel-copy panel-copy--mission">
    <h2 class="panel-title">
      <span class="panel-title__main">OUR</span>
      <span class="panel-title__sub">MISSION</span>
    </h2>
    <p class="panel-body">Lakemont Hydro Partners, Inc.'s mission is to produce and deliver portable drinking water and treat residential wastewater in a safe, reliable, efficient and environmentally sound manner. Our vision is to be the recognized performance leader of the water and wastewater utility industry. Being a performance leader means we will achieve operational excellence, industry-leading customer satisfaction and superior financial performance.</p>
  </section>

  <div class="page-label page-label--left">Inside Page</div>
  <div class="page-label page-label--right">Inside Page</div>
</div>
</body>
</html>
```